Sheriff Candidate needs a large yard sign

A candidate for Sheriff needs to have a sign to put in front of businesses and houses that advertise her candidacy.

Target Market(s)

Democrats, voters

Industry/Entity Type

Political

Font styles to use
Sans Serif

Colors
34a7d7
3276b5

Requirements
Must have
• Must have her picture
• Must have the words "Elect Dana Whitlock" - I'd like the name Dana to be smaller Whitlock. "Elect" and "Whitlock" should be the focus.
• at the bottom in a box "Paid for by the Committee to Elect Dana Whitlock"
Nice to have
• it would be good to have her logo as well.
• blue color for democrats and on a white background
Should not have
• pink color

```html
<!DOCTYPE html>
<html lang="en">
<head>
<meta charset="utf-8">
<title>Elect Dana Whitlock – Yard Sign</title>
<link rel="stylesheet" href="https://fonts.googleapis.com/css2?family=Fira+Sans+Extra+Condensed:wght@300;400;600;700&display=swap">
<style>
  :root {
    --sky-blue: #34a7d7;
    --party-blue: #3276b5;
    --ink: #0b0b0b;
    --paper: #ffffff;
    --steel: #5d5a58;
    --gold: #c59a2e;
    --backdrop: #e9ecef;
    --photo-light: #8c8a89;
    --photo-dark: #5f5c5b;
  }
  * { box-sizing: border-box; margin: 0; padding: 0; }
  html, body {
    width: 1200px; height: 1000px; overflow: hidden;
    background: var(--backdrop);
    font-family: "Fira Sans Extra Condensed", "Arial Narrow", sans-serif;
  }
  .yard-sign {
    position: absolute; left: 0; top: 162px;
    width: 1200px; height: 675px;
    background: var(--paper);
    overflow: hidden;
  }
  .sign-shapes { position: absolute; inset: 0; }
  .campaign-mark {
    position: absolute; left: 788px; top: 58px; width: 200px;
    display: flex; flex-direction: column; align-items: center; gap: 10px;
  }
  .campaign-mark__dot {
    width: 64px; height: 64px; border-radius: 50%; background: var(--gold);
  }
  .campaign-mark__name {
    color: var(--gold); font-weight: 600; font-size: 22px; letter-spacing: 1.5px;
    text-transform: uppercase; white-space: nowrap;
  }
  .headline {
    position: absolute; left: 640px; top: 0; width: 530px; height: 540px;
    color: var(--party-blue); font-size: 16px; white-space: nowrap;
  }
  .headline__elect {
    position: absolute; left: 24px; top: 254px;
    font-weight: 700; font-size: 116px; line-height: 1; letter-spacing: 1px;
  }
  .headline__first {
    position: absolute; left: 82px; top: 364px; width: 424px;
    display: flex; align-items: center; gap: 12px;
  }
  .headline__rule { flex: 1; height: 30px; display: flex; flex-direction: column; justify-content: space-between; }
  .headline__rule span { display: block; height: 2px; background: var(--party-blue); }
  .headline__first-name { font-weight: 400; font-size: 72px; line-height: 1; color: var(--sky-blue); }
  .headline__last {
    position: absolute; right: 22px; top: 422px;
    font-weight: 700; font-size: 104px; line-height: 1; letter-spacing: 0.5px;
  }
  .party-label {
    position: absolute; left: 593px; top: 545px;
    font-weight: 700; font-size: 40px; line-height: 1; color: var(--party-blue);
    letter-spacing: 0.5px; white-space: nowrap;
  }
  .platform {
    position: absolute; left: 802px; top: 545px;
    font-weight: 600; font-size: 40px; line-height: 1; color: var(--paper);
    letter-spacing: 1px; white-space: nowrap;
  }
  .disclaimer {
    position: absolute; right: 30px; top: 610px;
    display: flex; align-items: baseline; gap: 10px; color: var(--paper); white-space: nowrap;
  }
  .disclaimer__lead { font-weight: 300; font-size: 27px; }
  .disclaimer__committee { font-weight: 700; font-size: 42px; line-height: 1; }
</style>
</head>
<body>
  <main class="yard-sign">
    <svg class="sign-shapes" width="1200" height="675" viewBox="0 0 1200 675">
      <defs>
        <radialGradient id="portraitTone" cx="40%" cy="35%" r="75%">
          <stop offset="0" stop-color="var(--photo-light)"/>
          <stop offset="1" stop-color="var(--photo-dark)"/>
        </radialGradient>
      </defs>
      <path class="top-band" d="M520 0 H1200 V93 C1120 92 1060 90 1010 70 C950 45 830 45 780 62 C700 85 620 88 560 85 Z" fill="var(--sky-blue)"/>
      <path class="portrait" role="img" aria-label="Portrait photograph of candidate Dana Whitlock in a dark blazer against a grey studio backdrop"
            d="M0 0 H470 C555 90 600 220 590 330 C578 470 500 600 420 675 H0 Z" fill="url(#portraitTone)"/>
      <path class="portrait-arc portrait-arc--steel" d="M480 0 C568 95 612 225 602 335 C590 470 512 600 432 675" fill="none" stroke="var(--steel)" stroke-width="5"/>
      <path class="portrait-arc portrait-arc--blue" d="M494 0 C590 100 628 232 618 342 C605 480 530 600 450 675" fill="none" stroke="var(--party-blue)" stroke-width="4"/>
      <line class="party-rule" x1="540" y1="588" x2="780" y2="588" stroke="var(--ink)" stroke-width="4"/>
      <polygon class="platform-band" points="786,541 1200,541 1200,590 768,590" fill="var(--ink)"/>
      <path class="footer-band" d="M462 675 C488 650 505 622 520 595 H1200 V675 Z" fill="var(--sky-blue)"/>
    </svg>

    <div class="campaign-mark">
      <span class="campaign-mark__dot"></span>
      <span class="campaign-mark__name">Whitlock for Sheriff</span>
    </div>

    <h1 class="headline">
      <span class="headline__elect">ELECT</span>
      <span class="headline__first">
        <span class="headline__rule"><span></span><span></span><span></span></span>
        <span class="headline__first-name">DANA</span>
        <span class="headline__rule"><span></span><span></span><span></span></span>
      </span>
      <span class="headline__last">WHITLOCK</span>
    </h1>

    <p class="party-label">DEMOCRAT</p>
    <p class="platform">COMMUNITY POLICING</p>

    <p class="disclaimer">
      <span class="disclaimer__lead">Paid for by the Committee to</span>
      <span class="disclaimer__committee">ELECT DANA WHITLOCK</span>
    </p>
  </main>
</body>
</html>
```